Business Card Design

Its a residential construction company

Industry/Entity Type

Residential

Contact Information for Business Card

Belvora Homes Pty Ltd,
Dylan R Foster
BE (Civil), Grad.Dip Hwy, Eng. (QCTU), FTC.Aust,
Director, Belvora Homes Pty Ltd

PO Box 587, Arden, VIC, 3184. Tel: 048765 2231
email: dylan@belvorahomes.com

```html
<!DOCTYPE html>
<html lang="en">
<head>
<meta charset="utf-8">
<title>Belvora Homes Pty Ltd — Business Card</title>
<link rel="stylesheet" href="https://fonts.googleapis.com/css2?family=Tinos:wght@400;700&display=swap">
<style>
  :root {
    --stage: #4a3b2e;
    --card-top: #1a1a1a;
    --card-bottom: #050505;
    --text-light: #f4f4f4;
    --accent-coral: #ea6a60;
    --mark-blue: #4fb3dc;
  }
  * { margin: 0; padding: 0; box-sizing: border-box; }
  html, body {
    width: 1200px;
    height: 892px;
    overflow: hidden;
    background: var(--stage);
  }
  .stage {
    width: 1200px;
    height: 892px;
    display: flex;
    align-items: center;
    justify-content: center;
  }
  .card {
    position: relative;
    width: 470px;
    height: 770px;
    background: linear-gradient(160deg, var(--card-top) 0%, var(--card-bottom) 60%);
    border-radius: 4px;
    box-shadow: 0 18px 40px rgba(0,0,0,0.45);
    font-family: "Tinos", "Times New Roman", serif;
    color: var(--text-light);
  }
  .brand {
    position: absolute;
    top: 150px;
    left: 0;
    right: 0;
    display: flex;
    align-items: center;
    justify-content: center;
    gap: 14px;
  }
  .brand-square {
    width: 22px;
    height: 22px;
    background: var(--mark-blue);
  }
  .brand-name {
    font-size: 30px;
    font-weight: 700;
    font-variant: small-caps;
    letter-spacing: 1px;
    color: var(--text-light);
  }
  .person {
    position: absolute;
    top: 300px;
    left: 0;
    right: 0;
    text-align: center;
  }
  .person-name {
    font-size: 44px;
    font-weight: 700;
    color: var(--accent-coral);
    letter-spacing: 0.5px;
  }
  .person-role {
    margin-top: 6px;
    font-size: 19px;
  }
  .person-credentials {
    margin-top: 4px;
    font-size: 19px;
    line-height: 1.25;
  }
  .contact {
    position: absolute;
    left: 60px;
    bottom: 150px;
    font-size: 26px;
    line-height: 1.45;
    font-style: normal;
  }
</style>
</head>
<body>
  <main class="stage">
    <article class="card">
      <div class="brand">
        <span class="brand-square"></span>
        <span class="brand-name">Belvora Homes Pty Ltd</span>
      </div>
      <section class="person">
        <h1 class="person-name">Dylan R Foster</h1>
        <p class="person-role">Director</p>
        <p class="person-credentials">BE (Civil), Grad.Dip Hwy, Eng. (QCTU),<br>FTC.Aust</p>
      </section>
      <address class="contact">
        <div class="contact-phone">048765 2231</div>
        <div class="contact-email">dylan@belvorahomes.com</div>
        <div class="contact-post">PO Box 587, Arden, VIC, 3184</div>
      </address>
    </article>
  </main>
</body>
</html>
```